Quote Cards With TK May 2025 for Instagram

I would like to put these quotes over one of the pictures attached; Instagram (new size: 4:5 (1080 x 1350 pixels) One Quote per picture, and I want the quote to be bold or easy to read as well. I provided a few reference graphics that I really like as examples below. In very small letters at the bottom add @TKBarlowOnline

All of the pictures are attached; you can pick any photo and add one quote to it; but no stock photography

```html
<!DOCTYPE html>
<html lang="en">
<head>
<meta charset="utf-8">
<title>Quote Cards With TK</title>
<link href="https://fonts.googleapis.com/css2?family=Anton&family=Oswald:wght@400;500&display=swap" rel="stylesheet">
<style>
  :root{
    --page:#ffffff;
    --plum:#8b4f8a;
    --plum-soft:rgba(139,79,138,.45);
    --plum-clear:rgba(139,79,138,0);
    --ink:#ffffff;
  }
  *{margin:0;padding:0;box-sizing:border-box}
  html,body{width:849px;height:1200px;overflow:hidden;background:var(--page)}
  .sheet{position:relative;width:849px;height:1200px}
  .card{position:absolute;width:220px;height:275px;overflow:hidden;background:var(--plum)}
  .photo{position:absolute;inset:0}
  .shade{position:absolute;left:0;right:0;bottom:0;height:62%;
    background:linear-gradient(to bottom,var(--plum-clear),var(--plum-soft) 30%,var(--plum) 100%)}
  .panel{position:absolute;top:0;bottom:0;width:49%;
    background:linear-gradient(to bottom,rgba(139,79,138,.25),rgba(139,79,138,.7) 45%,var(--plum) 100%)}
  .panel.right{right:0}
  .panel.left{left:0}
  .quote{position:absolute;color:var(--ink);text-align:center;text-transform:uppercase;
    font-family:"Oswald",sans-serif;font-weight:400;font-size:15.5px;line-height:18px;letter-spacing:-.2px}
  .quote.wide{left:0;right:0}
  .quote.in-right{left:51%;right:0}
  .quote.in-left{left:0;width:49%}
  .quote b{display:block;font-family:"Anton",sans-serif;font-weight:400;font-size:19px;line-height:20.5px;letter-spacing:0}
  .handle{position:absolute;left:0;right:0;bottom:12px;text-align:center;color:var(--ink);
    font-family:"Oswald",sans-serif;font-weight:500;font-size:7px;letter-spacing:.1px}
  .ph-stage{background:linear-gradient(135deg,#3a2b7a,#c43d7a 45%,#f07a3a 70%,#5a3c9a)}
  .ph-kitchen{background:linear-gradient(180deg,#6b5a50,#3d302c 60%,#4a3a3a)}
  .ph-room{background:linear-gradient(90deg,#3a3536,#d8d2d0 60%,#b8a8b0)}
  .ph-court{background:linear-gradient(135deg,#8a6a6a,#d06aa0 40%,#5a4a5a)}
  .ph-dark{background:linear-gradient(90deg,#2e2626,#6a5e5e 50%,#3e3434)}
  .ph-arena{background:linear-gradient(180deg,#2a2440,#6a5030 50%,#4a3a3a)}
  .ph-studio{background:linear-gradient(90deg,#2a2a30,#6a6070 60%,#3a3440)}
  .ph-white{background:linear-gradient(180deg,#e8e6ea,#cfc8cf 60%,#b9a5bd)}
  .ph-lights{background:linear-gradient(135deg,#dcd8f0,#e7a0b8 40%,#e0a040 80%,#8a5a3a)}
  .ph-hills{background:linear-gradient(180deg,#b6cde0,#8a8a7a 50%,#5a4a44)}
</style>
</head>
<body>
<main class="sheet">

  <article class="card" style="left:84px;top:34px">
    <div class="photo ph-stage" role="img" aria-label="Photo of TK in a pink dress on a lit event stage"></div>
    <div class="shade"></div>
    <p class="quote wide" style="top:132px">That stubborn weight?<br>It's not your fault.<br>Your hormones<br>are to blame<br>and you're not alone;<b>But there is a fix.</b></p>
    <p class="handle">@TKBARLOWONLINE</p>
  </article>

  <article class="card" style="left:314px;top:34px">
    <div class="photo ph-kitchen" role="img" aria-label="Photo of TK pointing down in a kitchen"></div>
    <div class="shade"></div>
    <p class="quote wide" style="top:142px">Tired. Moody.<br>Stubborn belly fat.<br>Your hormones are<br>screaming for help!<b>Let's fix that.</b></p>
    <p class="handle">@TKBARLOWONLINE</p>
  </article>

  <article class="card" style="left:545px;top:34px">
    <div class="photo ph-room" role="img" aria-label="Photo of TK posing in a sheer top"></div>
    <div class="panel left"></div>
    <p class="quote in-left" style="top:45px">Your belly<br>isn't fat...<br>It's hormonal.<br>And here's<br>how to<br>fix it.<b>Comment<br>hormones</b>if nothing<br>is working.</p>
    <p class="handle">@TKBARLOWONLINE</p>
  </article>

  <article class="card" style="left:84px;top:320px">
    <div class="photo ph-court" role="img" aria-label="Photo of TK courtside holding a basketball"></div>
    <div class="panel right"></div>
    <p class="quote in-right" style="top:53px">The stubborn<br>belly fat<br>after 40?<br>It's not about<br>calories;<br>it's about<br>your hormones.<b>Here is<br>the fix!</b></p>
    <p class="handle">@TKBARLOWONLINE</p>
  </article>

  <article class="card" style="left:314px;top:320px">
    <div class="photo ph-dark" role="img" aria-label="Photo of TK in a satin top looking over her shoulder"></div>
    <div class="panel right"></div>
    <p class="quote in-right" style="top:42px">Flat tummy<br>in your 40s?<br>It's still<br>possible!<b>Comment<br>bye belly<br>to get the<br>10 secrets</b>to a flatter<br>tummy</p>
    <p class="handle">@TKBARLOWONLINE</p>
  </article>

  <article class="card" style="left:545px;top:320px">
    <div class="photo ph-arena" role="img" aria-label="Photo of TK standing on a basketball court"></div>
    <div class="panel right"></div>
    <p class="quote in-right" style="top:64px">Bloating.<br>Muffin top.<br>Puffy waistline.<br>Your body's<br>screaming<br>for a different<br>kind of fix.<b>Here it is</b></p>
    <p class="handle">@TKBARLOWONLINE</p>
  </article>

  <article class="card" style="left:84px;top:605px">
    <div class="photo ph-studio" role="img" aria-label="Photo of TK in a sheer black outfit"></div>
    <div class="panel right"></div>
    <p class="quote in-right" style="top:42px">You're doing<br>all the “right”<br>things,<br>but your<br>belly won't<br>go down?<b>Here's<br>what you<br>haven't<br>tried.</b></p>
    <p class="handle">@TKBARLOWONLINE</p>
  </article>

  <article class="card" style="left:314px;top:605px">
    <div class="photo ph-white" role="img" aria-label="Photo of TK in a white sweater dancing in a kitchen"></div>
    <div class="shade"></div>
    <p class="quote wide" style="top:148px">This 90-day plan helped<br>women over 40 slim down,<br>get a tiny waist and feel<br>sexy again.<b>You're next.</b></p>
    <p class="handle">@TKBARLOWONLINE</p>
  </article>

  <article class="card" style="left:545px;top:605px">
    <div class="photo ph-lights" role="img" aria-label="Photo of TK in a pink outfit among lights and sunflowers"></div>
    <div class="shade"></div>
    <p class="quote wide" style="top:107px">This is the secret<br>women over 40 are using<br>to get snatched;<br>without starving.<b>Comment skinny<br>to get<br>the exact plan.</b></p>
    <p class="handle">@TKBARLOWONLINE</p>
  </article>

  <article class="card" style="left:84px;top:891px">
    <div class="photo ph-hills" role="img" aria-label="Photo of TK outdoors with hills behind"></div>
    <div class="panel right"></div>
    <p class="quote in-right" style="top:40px">What worked<br>in your 30s<br>won't work<br>now.<b>Here's<br>what<br>actually<br>does.</b>Drop 30 pounds<br>in 3 months.</p>
    <p class="handle">@TKBARLOWONLINE</p>
  </article>

</main>
</body>
</html>
```